Satchel & Compass needs new business card design

I need a new business card design. I'm looking for out-of-the-box design which represents the freedom of being a location independent entrepreneur.
I offer coaching, retreats and trips.
I would like to see designs with and without the photo.
Colors I use are black (#000000), green (#25A796) and brown (#D7C38C)
Website satchelandcompass.com

Target Market(s)

location independent entrepreneurs, digital nomads, people looking to swap the 9 to 5 for a lifestyle business

Industry/Entity Type

Business

Contact Information for Business Card

Petra Varga
Your Lifestyle Business Coach, Retreat & Trip Leader
http://satchelandcompass.com
hello@satchelandcompass.com
Live a life you don't need a holiday from

Font styles to use
Serif
Sans Serif

Requirements
Must have
• One side should contain only the logo. I would also consider having the "Live a life you don't need a holiday from" on that side too (depending on how it looks)
• Please show both sides on the designs.

```html
<!DOCTYPE html>
<html lang="en">
<head>
<meta charset="utf-8">
<title>Satchel &amp; Compass – Business Card</title>
<link rel="stylesheet" href="https://fonts.googleapis.com/css2?family=Oswald:wght@300;400;500&display=swap">
<style>
  :root {
    --backdrop: #e6e6e6;
    --card-white: #f7f7f7;
    --card-dark: #1e2124;
    --brand-green: #0f8a78;
    --accent-green: #25a796;
    --brand-gold: #d7c38c;
    --ink: #1a1a1a;
    --text-light: #ffffff;
  }
  * { margin: 0; padding: 0; box-sizing: border-box; }
  html, body {
    width: 1200px; height: 576px; overflow: hidden;
    background: var(--backdrop);
    font-family: "Oswald", "Arial Narrow", sans-serif;
  }
  .canvas { position: relative; width: 1200px; height: 576px; }
  .card {
    position: absolute; top: 139px;
    width: 484px; height: 292px;
    border-radius: 8px; overflow: hidden;
  }
  /* Front */
  .card-front { left: 82px; background: linear-gradient(#fbfbfb, #ececec); }
  .front-name {
    position: absolute; left: 0; right: 0; top: 108px;
    text-align: center; font-weight: 400; font-size: 40px;
    letter-spacing: 1px; text-transform: uppercase; color: var(--ink);
  }
  .front-band {
    position: absolute; left: 0; right: 0; bottom: 0; height: 35px;
    background: var(--brand-green);
    color: var(--text-light); font-size: 13px; font-weight: 300;
    display: flex; align-items: center; justify-content: center;
  }
  /* Back */
  .card-back { left: 602px; background: var(--card-dark); }
  .back-photo { position: absolute; inset: 0; }
  .back-name {
    position: absolute; left: 28px; top: 34px;
    color: var(--brand-gold); font-size: 20px; font-weight: 500;
    text-transform: uppercase; letter-spacing: .3px;
  }
  .back-role {
    position: absolute; left: 28px; top: 63px;
    color: var(--text-light); font-size: 11.5px; font-weight: 300; line-height: 15px;
  }
  .back-contacts { position: absolute; left: 28px; top: 154px; list-style: none; }
  .back-contacts li {
    display: flex; align-items: center; gap: 8px;
    color: var(--text-light); font-size: 12px; font-weight: 300;
    height: 20px; margin-bottom: 1px;
  }
  .contact-icon { width: 12px; height: 12px; flex: none; }
  .social-mark { width: 10px; height: 10px; background: var(--accent-green); flex: none; margin-right: 1px; }
  .back-tagline {
    position: absolute; left: 28px; top: 236px;
    color: var(--accent-green); font-size: 13.5px; font-weight: 400;
  }
</style>
</head>
<body>
<div class="canvas">

  <section class="card card-front">
    <div class="front-name">Satchel &amp; Compass</div>
    <div class="front-band">www.satchelandcompass.com</div>
  </section>

  <section class="card card-back">
    <svg class="back-photo" viewBox="0 0 484 292" width="484" height="292">
      <defs>
        <linearGradient id="foliage" x1="0" y1="0" x2="1" y2="1">
          <stop offset="0" stop-color="#6f8a5a"/>
          <stop offset=".5" stop-color="#a9a98a"/>
          <stop offset="1" stop-color="#4f6b3e"/>
        </linearGradient>
      </defs>
      <path d="M300 0 Q276 6 262 40 Q242 110 258 180 Q272 250 300 292" fill="none" stroke="var(--accent-green)" stroke-width="5"/>
      <path role="img" aria-label="Photo of the coach sitting on a garden fence among trees, holding a small sign"
            d="M318 0 H484 V292 H294 Q262 250 254 180 Q246 100 270 40 Q288 8 318 0 Z" fill="url(#foliage)"/>
    </svg>

    <div class="back-name">Petra Varga</div>
    <div class="back-role">Your Lifestyle Business Coach<br>Retreat &amp; Trip Leader</div>

    <ul class="back-contacts">
      <li>
        <svg class="contact-icon" viewBox="0 0 12 12"><rect x="0.5" y="2.5" width="11" height="7" fill="var(--accent-green)"/><path d="M0.5 2.5 L6 7 L11.5 2.5" fill="none" stroke="var(--card-dark)" stroke-width="1"/></svg>
        hello@satchelandcompass.com
      </li>
      <li>
        <svg class="contact-icon" viewBox="0 0 12 12"><circle cx="6" cy="6" r="5.2" fill="none" stroke="var(--accent-green)" stroke-width="1.2"/><ellipse cx="6" cy="6" rx="2.2" ry="5.2" fill="none" stroke="var(--accent-green)" stroke-width="1"/><line x1="0.8" y1="6" x2="11.2" y2="6" stroke="var(--accent-green)" stroke-width="1"/></svg>
        www.satchelandcompass.com
      </li>
      <li>
        <span class="social-mark"></span>
        /satchelandcompass
      </li>
    </ul>

    <div class="back-tagline">Live a life you don’t need a holiday from</div>
  </section>

</div>
</body>
</html>
```